" Atualmente somos dois sócios com experiência no mercado financeiro. A empresa foi fundada em 2016 e desde o início nossos escopo de trabalho se resume a captar clientes para processos de fusões e aquisições, seja para venda parcial ou total das empresas de nossos clientes. Desde a criação da empresa concluímos 3 transações importantes, além de diversas assessorias de valuation (avaliação de valor de empresas) e consultoria financeira. "

```html
<!DOCTYPE html>
<html lang="pt-BR">
<head>
<meta charset="UTF-8">
<title>Luma Capital — Envelopes</title>
<link href="https://fonts.googleapis.com/css2?family=Montserrat:wght@300;400;600&display=swap" rel="stylesheet">
<style>
  :root {
    --backdrop: #d3d4d6;
    --paper: #fbfbfb;
    --navy: #14304a;
    --navy-line: #1e3d5c;
    --gold: #b9995b;
    --light-text: #c9d1da;
  }
  html, body {
    margin: 0;
    padding: 0;
    width: 1200px;
    height: 1200px;
    overflow: hidden;
    background: var(--backdrop);
    font-family: "Montserrat", sans-serif;
  }
  .canvas {
    position: relative;
    width: 1200px;
    height: 1200px;
  }
  .envelope {
    position: absolute;
    left: 100px;
    width: 1000px;
    height: 500px;
    box-shadow: 0 14px 30px rgba(0,0,0,0.18);
  }
  .envelope-front {
    top: 70px;
    background: var(--paper);
  }
  .envelope-back {
    top: 630px;
    background: var(--navy);
    overflow: hidden;
  }
  .brand {
    position: absolute;
    display: flex;
    align-items: center;
    gap: 14px;
    font-weight: 600;
    letter-spacing: 0.06em;
    white-space: nowrap;
  }
  .brand-mark {
    display: block;
    border-radius: 0;
  }
  .envelope-front .brand {
    right: 70px;
    bottom: 60px;
    font-size: 38px;
    color: var(--navy);
  }
  .envelope-front .brand-mark {
    width: 30px;
    height: 30px;
    background: var(--gold);
  }
  .flap {
    position: absolute;
    inset: 0;
  }
  .side-contacts {
    position: absolute;
    left: 36px;
    top: 50px;
    font-size: 12px;
    line-height: 1.9;
    color: var(--light-text);
    font-weight: 400;
  }
  .side-contacts .row {
    display: flex;
    align-items: center;
    gap: 8px;
  }
  .side-contacts .dot {
    width: 9px;
    height: 9px;
    border-radius: 50%;
    background: var(--gold);
  }
  .envelope-back .brand {
    right: 60px;
    bottom: 150px;
    font-size: 26px;
    color: var(--gold);
  }
  .envelope-back .brand-mark {
    width: 20px;
    height: 20px;
    background: var(--gold);
  }
  .back-divider {
    position: absolute;
    right: 60px;
    bottom: 136px;
    width: 250px;
    height: 1px;
    background: var(--gold);
  }
  .address-block {
    position: absolute;
    right: 60px;
    bottom: 48px;
    width: 250px;
    font-size: 12px;
    line-height: 1.7;
    color: var(--light-text);
    text-align: right;
  }
</style>
</head>
<body>
<main class="canvas">

  <section class="envelope envelope-front" aria-label="Frente do envelope">
    <div class="brand">
      <span class="brand-mark"></span>
      <span class="brand-name">LUMA CAPITAL</span>
    </div>
  </section>

  <section class="envelope envelope-back" aria-label="Verso do envelope">
    <svg class="flap" width="1000" height="500" viewBox="0 0 1000 500" aria-hidden="true">
      <polyline points="0,0 110,190 890,190 1000,0" fill="none" stroke="var(--navy-line)" stroke-width="2"/>
      <line x1="0" y1="500" x2="330" y2="260" stroke="var(--navy-line)" stroke-width="2"/>
      <line x1="1000" y1="500" x2="670" y2="260" stroke="var(--navy-line)" stroke-width="2"/>
    </svg>

    <div class="side-contacts">
      <div class="row"><span class="dot"></span>contato@lumacapital.com.br</div>
      <div class="row"><span class="dot"></span>lumacapital.com.br</div>
    </div>

    <div class="brand">
      <span class="brand-mark"></span>
      <span class="brand-name">LUMA CAPITAL</span>
    </div>
    <div class="back-divider"></div>
    <address class="address-block" style="font-style:normal">
      (31) 3000-0000<br>
      contato@lumacapital.com.br<br>
      Avenida Exemplo, 100 - Sala 20<br>
      30100-000 Belo Horizonte
    </address>
  </section>

</main>
</body>
</html>
```